Saltmarsh Valley Lending Flyer

I would like our main long logo with the bird and words Saltmarsh Valley Lending with pictures of what we finance along the bottom.
Car , 4x4 , boat, excavator , Cash Loans and houses
Needs to look good on leaflet and large signage.
Simple but cool looking so it stands out.

```html
<!DOCTYPE html>
<html lang="en">
<head>
<meta charset="UTF-8">
<title>Saltmarsh Valley Lending Flyer</title>
<link href="https://fonts.googleapis.com/css2?family=Oswald:wght@400;500;600&family=Open+Sans:wght@400;600;700&display=swap" rel="stylesheet">
<style>
  :root {
    --orange: #f47a20;
    --dark: #2a2a2a;
    --dark-2: #3a3a3a;
    --ink: #2b2b2b;
    --white: #ffffff;
    --muted: #d9d9d9;
  }
  * { box-sizing: border-box; margin: 0; padding: 0; }
  html, body { width: 746px; height: 1200px; overflow: hidden; background: var(--white); }
  .flyer {
    position: relative; width: 746px; height: 1200px; overflow: hidden;
    background: radial-gradient(ellipse at 50% 45%, var(--dark-2) 0%, var(--dark) 70%);
    font-family: "Open Sans", sans-serif;
  }
  .header-shape { position: absolute; top: 0; left: 0; width: 746px; height: 230px; }
  .brand {
    position: absolute; top: 78px; left: 0; width: 746px;
    display: flex; justify-content: center; align-items: center; gap: 16px;
  }
  .brand-mark { width: 30px; height: 30px; background: var(--orange); }
  .brand-name {
    font-family: "Oswald", sans-serif; font-weight: 400; font-size: 34px;
    letter-spacing: 2px; text-transform: uppercase; color: var(--ink);
  }
  .headline {
    position: absolute; top: 262px; left: 0; width: 746px; text-align: center;
    font-family: "Oswald", sans-serif; font-weight: 400; font-size: 50px; line-height: 1.05;
    text-transform: uppercase; color: var(--white);
  }
  .headline .accent { display: block; color: var(--orange); font-weight: 500; }
  .intro {
    position: absolute; top: 392px; left: 120px; width: 506px; text-align: center;
    font-size: 14px; line-height: 1.45; color: var(--muted);
  }
  .services-title {
    position: absolute; top: 498px; left: 0; width: 746px; text-align: center;
    font-family: "Oswald", sans-serif; font-weight: 500; font-size: 36px;
    text-transform: uppercase; color: var(--white);
  }
  .services-title .accent { color: var(--orange); }
  .tile {
    position: absolute; border: 3px solid #e6e6e6; overflow: hidden;
  }
  .tile-label {
    position: absolute; left: 0; right: 0; bottom: 0; height: 34px;
    display: flex; align-items: center; justify-content: center; text-align: center;
    background: linear-gradient(to top, rgba(0,0,0,.75), rgba(0,0,0,0));
    font-weight: 700; font-size: 15px; line-height: 1.1; text-transform: uppercase; color: var(--white);
  }
  .tile-car { left: 48px; top: 580px; width: 212px; height: 200px;
    background: linear-gradient(180deg, #6f9fd3 0%, #a8c2d8 40%, #8a3a2a 60%, #5c5650 100%); }
  .tile-boat { left: 48px; top: 788px; width: 212px; height: 140px;
    background: linear-gradient(180deg, #b8c8d4 0%, #8fa7b8 45%, #6aa06a 70%, #5d4a80 100%); }
  .tile-4x4 { left: 268px; top: 580px; width: 212px; height: 140px;
    background: linear-gradient(180deg, #aab8a8 0%, #3f6a45 45%, #2e4a33 75%, #6a7a5a 100%); }
  .tile-excavator { left: 268px; top: 728px; width: 212px; height: 200px;
    background: linear-gradient(160deg, #e9e2f2 0%, #c9b8e0 25%, #e3b53a 55%, #8a6a3a 100%); }
  .tile-houses { left: 488px; top: 580px; width: 212px; height: 348px;
    background: linear-gradient(180deg, #c9d4de 0%, #8ea2b6 40%, #4d6073 75%, #33414f 100%); }
  .tile-houses .tile-label { height: 60px; }
  .contact-band { position: absolute; left: 0; top: 1090px; width: 746px; height: 110px; }
  .phone {
    position: absolute; top: 1097px; left: 0; width: 746px;
    display: flex; justify-content: center; align-items: center; gap: 8px;
    font-family: "Oswald", sans-serif; font-weight: 500; font-size: 30px; color: var(--white);
  }
  .footer {
    position: absolute; top: 1152px; left: 0; width: 746px; height: 48px;
    display: flex; justify-content: center; align-items: center; gap: 12px;
    font-size: 11px; color: var(--ink);
  }
  .footer-item { display: flex; align-items: center; gap: 6px; }
  .divider { width: 1px; height: 18px; background: var(--ink); }
</style>
</head>
<body>
<main class="flyer">
  <svg class="header-shape" viewBox="0 0 746 230" aria-hidden="true">
    <polygon points="0,0 746,0 746,120 373,215 0,120" fill="#ffffff"/>
    <polygon points="0,120 373,215 373,222 0,127" fill="#000" opacity=".15"/>
  </svg>

  <div class="brand">
    <span class="brand-mark"></span>
    <span class="brand-name">Saltmarsh Valley Lending</span>
  </div>

  <h1 class="headline">Experts in mortgage<span class="accent">Broking and lending</span></h1>

  <p class="intro">Making a big purchase can be a daunting experience. Whether you are re-financing, down-sizing, investing or buying your first home, there is always so much to consider when taking out a loan.</p>

  <h2 class="services-title">Our <span class="accent">Services</span></h2>

  <div class="tile tile-car" role="img" aria-label="Photo of a red ute parked on a sunny street"><span class="tile-label">Car</span></div>
  <div class="tile tile-boat" role="img" aria-label="Photo of a colourful speedboat on the water"><span class="tile-label">Boat</span></div>
  <div class="tile tile-4x4" role="img" aria-label="Photo of a green four wheel drive"><span class="tile-label">4x4</span></div>
  <div class="tile tile-excavator" role="img" aria-label="Photo of a yellow excavator on a work site"><span class="tile-label">Excavator</span></div>
  <div class="tile tile-houses" role="img" aria-label="Photo of city towers and apartment buildings"><span class="tile-label">Cash loans and<br>houses</span></div>

  <svg class="contact-band" viewBox="0 0 746 110" aria-hidden="true">
    <polygon points="220,0 526,0 556,56 190,56" fill="#f47a20"/>
    <rect x="0" y="56" width="746" height="6" fill="#f47a20"/>
    <rect x="0" y="62" width="746" height="48" fill="#ffffff"/>
  </svg>

  <div class="phone">
    <svg width="26" height="26" viewBox="0 0 24 24" aria-hidden="true">
      <circle cx="12" cy="12" r="10.5" fill="none" stroke="#fff" stroke-width="2"/>
      <path d="M8.5 7.5c.5-.5 1.2-.4 1.5.1l1 1.6c.3.4.2 1-.2 1.3l-.6.5c.5 1.2 1.5 2.2 2.7 2.7l.5-.6c.3-.4.9-.5 1.3-.2l1.6 1c.5.3.6 1 .1 1.5l-.7.7c-.8.8-2 .9-3 .3-2.3-1.3-4-3-5.3-5.3-.6-1-.5-2.2.3-3z" fill="#fff"/>
    </svg>
    <span>08 5550 2718</span>
  </div>

  <div class="footer">
    <span class="footer-item">
      <svg width="12" height="14" viewBox="0 0 12 16" aria-hidden="true"><path d="M6 0a6 6 0 0 0-6 6c0 4.5 6 10 6 10s6-5.5 6-10a6 6 0 0 0-6-6zm0 8.5A2.5 2.5 0 1 1 6 3.5a2.5 2.5 0 0 1 0 5z" fill="#f47a20"/></svg>
      Unit 4, 27 Harbour Lane Eastbank NT 0810
    </span>
    <span class="divider"></span>
    <span class="footer-item">
      <svg width="14" height="14" viewBox="0 0 16 16" aria-hidden="true"><circle cx="8" cy="8" r="7" fill="none" stroke="#f47a20" stroke-width="1.6"/><ellipse cx="8" cy="8" rx="3" ry="7" fill="none" stroke="#f47a20" stroke-width="1.3"/><line x1="1" y1="8" x2="15" y2="8" stroke="#f47a20" stroke-width="1.3"/></svg>
      www.svlending.com.au
    </span>
    <span class="divider"></span>
    <span class="footer-item">
      <svg width="15" height="11" viewBox="0 0 16 12" aria-hidden="true"><rect width="16" height="12" rx="1" fill="#f47a20"/><path d="M1 1l7 6 7-6" fill="none" stroke="#fff" stroke-width="1.4"/></svg>
      info@svlending.com.au
    </span>
  </div>
</main>
</body>
</html>
```